Business school needs a web design

Who We are:
KRVT is a small business school that offers programs in Project Management. The school is based in West Africa and welcomes students from the whole area. Our aim is to become one of the reference business schools in Africa.

Project Brief:
The site will include all informations relevant for different types of visitors that we have: actual and future students, companies, mass media, future employees, ect. It will present information about subscription, list of programs, presentation of the school and its team,etc.

What We want:
This competition is for Design only no coding! We need design for two pages.
We did some wireframing for the home page and the list of programs page. We made them just to show how we imagine the website would look like. But we encourage creative designs, so you don't have to stick to the wireframe models.

Sites We like:
http://www.ravenmoorcollege.example/
http://www.belvantis.example/fr/etudes.html
http://www.qtl.example/mba/Pages/default.aspx

Color schemes
The logo of the school is red and black. So the color scheme of the website should match that. For the rest, it is opened to your imagination.
Updates

The payment for the project is now garanteed. Good luck to you all !

Target Market(s)

The target market is diversified because we have students of different ages, also company representatives or employees that might visit the website for recruitment purposes. But the majority of our audience should be aged between 20 - 30 years.

Industry/Entity Type

Small Business

Requirements
Must have
• The design must include two pages: a home page and another interior page : might be the list of programs or any other page relevant to the domain. The Home page must include a slide show at the beginning.
The background page must be white.
Nice to have
• The use of flat design for this project is preferred.
The use of Pelican scaffold as a base for the design is an asset.

```html
<!DOCTYPE html>
<html lang="fr">
<head>
<meta charset="utf-8">
<title>KRVT – Programmes et Formations</title>
<link href="https://fonts.googleapis.com/css2?family=Open+Sans:wght@300;400;600;700&display=swap" rel="stylesheet">
<style>
:root{
  --red:#c40000;
  --ink:#222;
  --text:#444;
  --muted:#777;
  --line:#d6d6d6;
  --foot-head:#555;
  --foot-body:#e6e6e6;
  --player:#c8c8c8;
}
*{box-sizing:border-box;margin:0;padding:0}
html,body{width:1020px;height:1200px;overflow:hidden;background:#fff}
body{font-family:"Open Sans",sans-serif;color:var(--text);position:relative}
.abs{position:absolute}
a{color:inherit;text-decoration:none}

/* header */
.brand{left:95px;top:10px;display:flex;align-items:center;gap:6px;font-weight:700;font-size:24px;color:var(--red)}
.brand-mark{width:18px;height:18px;background:var(--red);border-radius:50%}
.util{right:86px;top:15px;font-size:11px;color:var(--muted);display:flex}
.util span{padding:0 7px;border-left:1px solid var(--line)}
.util span:first-child{border:0}
.util span:last-child{padding-right:0}
.search{left:769px;top:45px;width:165px;height:23px;border:1px solid #ccc;border-radius:3px;display:flex;overflow:hidden}
.search span{flex:1;font-size:10px;color:var(--muted);padding:4px 8px}
.search i{width:29px;background:var(--red);display:flex;align-items:center;justify-content:center}
.nav{right:86px;top:84px;display:flex;font-size:12px;color:var(--ink);text-transform:uppercase}
.nav span{padding:0 7px;border-left:1px solid var(--line);line-height:14px}
.nav span:first-child{border:0;color:var(--red)}
.nav span:last-child{padding-right:0}

/* hero */
.hero{left:0;top:107px;width:1020px;height:263px;background:linear-gradient(90deg,#c40000 0%,#c00000 60%,#b80404 100%)}
.hero-title{left:94px;top:174px;font-weight:300;font-size:27px;color:#fff}
.hero-copy{left:94px;top:218px;font-size:12px;line-height:24.7px;color:#fff}

/* breadcrumb */
.crumbs{left:0;top:370px;width:1020px;height:30px;border-bottom:1px solid var(--line);font-size:11px;padding:8px 94px}
.crumbs .home{color:var(--red)}
.crumbs .sep{font-size:8px;margin:0 5px;color:#555}

/* intro */
.page-title{left:0;top:414px;width:1020px;text-align:center;font-size:19px;font-weight:600;color:#111}
.intro{left:95px;top:448px;width:840px;text-align:center;font-size:11.5px;line-height:19px;font-weight:300;color:#444}
.rule{left:94px;width:840px;height:1px;background:var(--line)}

/* tracks */
.track{top:545px;width:268px}
.track h2{font-size:14px;font-weight:700;color:#111;letter-spacing:.2px;margin-bottom:9px}
.media{width:268px;height:160px}
.player{height:31px;background:var(--player);display:flex;align-items:center;padding:0 8px;gap:9px}
.bar{flex:1;height:8px;border:1.5px solid #111;background:#fff;position:relative}
.bar::before{content:"";position:absolute;left:0;top:0;bottom:0;width:41%;background:#111}
.track h3{font-size:12px;font-weight:700;color:#111;margin:11px 1px 2px}
.track p{font-size:10.5px;line-height:16px;margin-left:1px}

/* offered */
.sub-title{left:96px;top:836px;font-size:14px;font-weight:700;color:#111}
.offer{width:400px;height:56px;display:flex;gap:11px}
.offer .thumb{width:75px;height:56px;flex:none}
.offer h4{font-size:11px;font-weight:700;color:#111;line-height:14px;margin-top:-1px}
.offer p{font-size:11px;line-height:16px;margin-top:1px}

/* share rail */
.share{left:987px;top:573px;width:33px;border:1px solid var(--line);border-right:0;background:#fff}
.share div{height:34px;border-top:1px solid var(--line);display:flex;align-items:center;justify-content:center}
.share div:first-child{border-top:0;height:41px}

/* footer */
.foot-head{left:0;top:1018px;width:1020px;height:26px;background:var(--foot-head)}
.foot-body{left:0;top:1044px;width:1020px;height:130px;background:var(--foot-body)}
.foot-base{left:0;top:1174px;width:1020px;height:26px;background:var(--foot-body);border-top:1px solid #ccc;font-size:9.5px;color:#666;padding:6px 95px}
.fcol{top:1024px;font-size:10px;color:#333}
.fcol h5{font-size:12px;font-weight:600;color:#fff;margin-bottom:15px;display:flex;align-items:center;gap:6px}
.fcol li{list-style:none;line-height:18px}
.fcol .strong{font-weight:600}
.phone{display:flex;align-items:center;gap:6px;font-weight:600;margin-top:6px}
.news{font-size:10px;line-height:18px;text-align:justify;width:153px}
.news-form{display:flex;margin-top:13px;width:153px;height:26px}
.news-form span{flex:1;background:#fff;border:1px solid #ccc}
.news-form b{background:var(--red);color:#fff;font-size:10.5px;padding:5px 7px}
.social{display:flex;gap:10px;margin-top:2px}
.social span{width:22px;height:22px;border:2px solid #999;border-radius:50%}
</style>
</head>
<body>

<header>
  <div class="abs brand"><span class="brand-mark"></span>KRVT</div>
  <nav class="abs util"><span>Repertoire du personel</span><span>Blogue</span><span>Salle de presse</span><span>Nous joindre</span><span>Francais</span></nav>
  <div class="abs search"><span>Search</span><i><svg width="13" height="13" viewBox="0 0 13 13"><circle cx="5.5" cy="5.5" r="4" fill="none" stroke="#fff" stroke-width="1.8"/><line x1="8.5" y1="8.5" x2="12" y2="12" stroke="#fff" stroke-width="1.8"/></svg></i></div>
  <nav class="abs nav"><span>A propos de l'KRVT</span><span>Programmes et formaions</span><span>Etudiants</span><span>Nouvelles et evenements</span><span>Enterprises</span></nav>
</header>

<section class="abs hero" role="img" aria-label="Red banner with faint silhouettes of business people"></section>
<h1 class="abs hero-title">Lorem Ipsum is simply dummy text</h1>
<p class="abs hero-copy">Lorem Ipsum is simply dummy text of the printing and typesetting industry.<br>Lorem Ipsum has been the industry's standard dummy text ever since the 1500s,<br>when an unknown printer took a galley of type and scrambled it to make a type specimen book.<br>It has survived not only five centuries</p>

<div class="abs crumbs"><span class="home">Accueil</span><span class="sep">▶</span>Programmes et Formations</div>

<h2 class="abs page-title">PROGRAMMES ET FORMATIONS</h2>
<p class="abs intro">Lorem Ipsum is simply dummy text of the printing and typesetting industry. Lorem Ipsum has been the industry's standard dummy text ever since the 1500s, when an unknown printer took a galley of type and scrambled it to make a type specimen book. It has survived not only five centuries, but also the leap into electronic typesetting, remaining essentially unchanged.</p>
<div class="abs rule" style="top:523px"></div>

<article class="abs track" style="left:95px">
  <h2>FORMATIONS DIPLOMANTES</h2>
  <div class="media" role="img" aria-label="Video still: presenter at a flip chart with seated students" style="background:linear-gradient(135deg,#e8e8e8,#8a8a8a 60%,#3a3a3a)"></div>
  <div class="player"><svg width="18" height="18" viewBox="0 0 18 18"><circle cx="9" cy="9" r="7.5" fill="none" stroke="#111" stroke-width="1.6"/><path d="M7 5.5v7l5.5-3.5z" fill="#111"/></svg><div class="bar"></div><svg width="18" height="16" viewBox="0 0 18 16"><path d="M1 5h4l5-4v14l-5-4H1z" fill="#111"/><path d="M12 5q2 3 0 6M14 3q4 5 0 10" fill="none" stroke="#111" stroke-width="1.5"/></svg><svg width="16" height="16" viewBox="0 0 16 16" fill="#111"><path d="M1 1h5L1 6zM15 1v5L10 1zM1 15v-5l5 5zM15 15h-5l5-5z"/></svg></div>
  <h3>Lorem Ipsum</h3>
  <p>Lorem Ipsum is simply dummy text of the printing and industry. Lorem Ipsum has been the industry'.</p>
</article>

<article class="abs track" style="left:381px">
  <h2>CERTIFICATS PROFESSIONNELS</h2>
  <div class="media" role="img" aria-label="Video still: two professionals reviewing documents" style="background:linear-gradient(135deg,#b8b8c0,#e6e2de 50%,#6a6a72)"></div>
  <div class="player"><svg width="18" height="18" viewBox="0 0 18 18"><circle cx="9" cy="9" r="7.5" fill="none" stroke="#111" stroke-width="1.6"/><path d="M7 5.5v7l5.5-3.5z" fill="#111"/></svg><div class="bar"></div><svg width="18" height="16" viewBox="0 0 18 16"><path d="M1 5h4l5-4v14l-5-4H1z" fill="#111"/><path d="M12 5q2 3 0 6M14 3q4 5 0 10" fill="none" stroke="#111" stroke-width="1.5"/></svg><svg width="16" height="16" viewBox="0 0 16 16" fill="#111"><path d="M1 1h5L1 6zM15 1v5L10 1zM1 15v-5l5 5zM15 15h-5l5-5z"/></svg></div>
  <h3>Lorem Ipsum</h3>
  <p>Lorem Ipsum is simply dummy text of the printing and industry. Lorem Ipsum has been the industry'.</p>
</article>

<article class="abs track" style="left:666px">
  <h2>FORMATIONS A LA CARTE</h2>
  <div class="media" role="img" aria-label="Video still: participants working on laptops at a workshop" style="background:linear-gradient(135deg,#c9a48a,#7f8a96 50%,#d8d0c4)"></div>
  <div class="player"><svg width="18" height="18" viewBox="0 0 18 18"><circle cx="9" cy="9" r="7.5" fill="none" stroke="#111" stroke-width="1.6"/><path d="M7 5.5v7l5.5-3.5z" fill="#111"/></svg><div class="bar"></div><svg width="18" height="16" viewBox="0 0 18 16"><path d="M1 5h4l5-4v14l-5-4H1z" fill="#111"/><path d="M12 5q2 3 0 6M14 3q4 5 0 10" fill="none" stroke="#111" stroke-width="1.5"/></svg><svg width="16" height="16" viewBox="0 0 16 16" fill="#111"><path d="M1 1h5L1 6zM15 1v5L10 1zM1 15v-5l5 5zM15 15h-5l5-5z"/></svg></div>
  <h3>Lorem Ipsum</h3>
  <p>Lorem Ipsum is simply dummy text of the printing and industry. Lorem Ipsum has been the industry'.</p>
</article>

<h2 class="abs sub-title">PROGRAMMES OFFERTS</h2>
<div class="abs rule" style="top:864px"></div>

<div class="abs offer" style="left:95px;top:879px"><div class="thumb" role="img" aria-label="Student portrait outdoors" style="background:linear-gradient(135deg,#7a8a6a,#d9c2b0)"></div><div><h4>Lorem Ipsum</h4><p>Lorem Ipsum is simply dummy text of the printing and typesetting industry</p></div></div>
<div class="abs offer" style="left:530px;top:879px"><div class="thumb" role="img" aria-label="Colleagues in an office meeting" style="background:linear-gradient(135deg,#e0d6cc,#8a7a6e)"></div><div><h4>Lorem Ipsum</h4><p>Lorem Ipsum is simply dummy text of the printing and typesetting industry</p></div></div>
<div class="abs offer" style="left:95px;top:949px"><div class="thumb" role="img" aria-label="Group of students around a table" style="background:linear-gradient(135deg,#4a4a4a,#d8d8d8)"></div><div><h4>Lorem Ipsum</h4><p>Lorem Ipsum is simply dummy text of the printing and typesetting industry</p></div></div>
<div class="abs offer" style="left:530px;top:949px"><div class="thumb" role="img" aria-label="Student writing at a desk" style="background:linear-gradient(135deg,#f0f0f0,#9a9aa6)"></div><div><h4>Lorem Ipsum</h4><p>Lorem Ipsum is simply dummy text of the printing and typesetting industry</p></div></div>

<aside class="abs share" aria-label="Partager">
  <div><svg width="16" height="16"><circle cx="8" cy="8" r="6.5" fill="none" stroke="#888" stroke-width="1.3"/></svg></div>
  <div><svg width="16" height="16"><circle cx="8" cy="8" r="6.5" fill="none" stroke="#888" stroke-width="1.3"/></svg></div>
  <div><svg width="16" height="16"><circle cx="8" cy="8" r="6.5" fill="none" stroke="#888" stroke-width="1.3"/></svg></div>
  <div><svg width="18" height="16" viewBox="0 0 18 16" fill="none" stroke="#888" stroke-width="1.3"><rect x="4" y="1" width="10" height="4"/><rect x="1" y="5" width="16" height="7" rx="1"/><rect x="4" y="9" width="10" height="6" fill="#fff"/></svg></div>
  <div><svg width="18" height="16" viewBox="0 0 18 16" fill="none" stroke="#888" stroke-width="1.3"><ellipse cx="9" cy="7" rx="7.5" ry="5.5"/><path d="M4 11l-2 4 5-2.5"/></svg></div>
</aside>

<footer>
  <div class="abs foot-head"></div>
  <div class="abs foot-body"></div>
  <div class="abs fcol" style="left:95px"><h5>Suivez-nous</h5><div class="social"><span></span><span></span><span></span><span></span></div></div>
  <div class="abs fcol" style="left:260px"><h5>A propos</h5><ul><li>A propos de l'KRVT</li><li>Admissions</li><li>Calendrier de L'ecole</li><li>Offres d'emploi</li><li>Offres d'emploi</li><li>Repertoire du personnel</li></ul></div>
  <div class="abs fcol" style="left:425px"><h5>Etudiants</h5><ul><li>Accueil - Etudiants</li><li>Programmes et Formations</li><li>Vie etudiante</li><li class="strong" style="margin-top:5px">Enterprises</li><li class="strong">Blogue</li></ul></div>
  <div class="abs fcol" style="left:598px"><h5>KRVT</h5><ul><li>14, RUE DES ACACIAS</li><li>Ancienne route, pres du Jardin</li><li>des Petits</li></ul>
    <div class="phone"><svg width="8" height="16" viewBox="0 0 8 16"><path d="M6 1Q1 8 6 15" fill="none" stroke="#888" stroke-width="3" stroke-linecap="round"/></svg>(221) 30 000 12 34</div>
    <div class="phone"><svg width="8" height="16" viewBox="0 0 8 16"><path d="M6 1Q1 8 6 15" fill="none" stroke="#888" stroke-width="3" stroke-linecap="round"/></svg>(221) 70 000 56 78</div></div>
  <div class="abs fcol" style="left:782px"><h5>Infolettre <svg width="18" height="12" viewBox="0 0 18 12" fill="none" stroke="#fff" stroke-width="1"><rect x=".5" y=".5" width="17" height="11"/><path d="M.5 .5l8.5 6 8.5-6"/></svg></h5><p class="news">Lorem Ipsum is simply dummy text of the printing and typesetting industry.</p><div class="news-form"><span></span><b>ENVOYER</b></div></div>
  <div class="abs foot-base">© KRVT, 2013 Tous driots reserves</div>
</footer>

</body>
</html>
```